New Business Card

Would like a shiny card with Metallic logo raised on th front. Address 418 Kestwick Lane, Toronto Ontario M4T2B8, phone 416 555 0382, email kmvc@lorentel.ca and web www.kmvc.ca on the back in right and left lower corners balanced. Top of back should say Personalized Care for Pet's and their People centered. Leaving space on the back to write. Horizontal placement

```html
<!DOCTYPE html>
<html lang="en">
<head>
<meta charset="utf-8">
<title>Kestwick Mews Animal Clinic – Business Card</title>
<link rel="stylesheet" href="https://fonts.googleapis.com/css2?family=Roboto:wght@400;500;700&display=swap">
<style>
  :root {
    --stage: #e9e7e3;
    --card-dark: #4e4e50;
    --card-light: #ffffff;
    --ink-light: #ffffff;
    --ink-dark: #3a3a3a;
    --rule-light: #d2d2d2;
    --rule-on-dark: #cfcfcf;
    --shadow: rgba(0, 0, 0, 0.22);
  }
  * { box-sizing: border-box; margin: 0; padding: 0; }
  html, body {
    width: 1200px; height: 900px; overflow: hidden;
    background: var(--stage);
    font-family: "Roboto", Arial, sans-serif;
  }
  .stage {
    position: relative; width: 1200px; height: 900px;
    display: flex; flex-direction: column; align-items: center;
    justify-content: center; gap: 42px;
  }
  .card {
    position: relative; width: 620px; height: 354px;
    border-radius: 22px; overflow: hidden;
    box-shadow: 0 12px 30px var(--shadow);
  }

  /* Back side */
  .card-back { background: var(--card-light); }
  .card-back .watermark-area {
    position: absolute; left: 150px; top: 40px; width: 330px; height: 280px;
    border-radius: 50%;
    background: radial-gradient(ellipse at center, rgba(0,0,0,0.07) 0%, rgba(0,0,0,0.03) 55%, rgba(0,0,0,0) 75%);
  }
  .card-back .tagline {
    position: absolute; top: 36px; left: 0; right: 0; text-align: center;
    font-size: 15px; font-weight: 500; color: var(--ink-dark); letter-spacing: 0.2px;
  }
  .card-back .write-lines {
    position: absolute; left: 46px; right: 46px; top: 78px;
    display: flex; flex-direction: column; gap: 48px;
  }
  .card-back .write-lines span {
    display: block; height: 1px; background: var(--rule-light);
  }

  /* Front side */
  .card-front { background: var(--card-dark); color: var(--ink-light); }
  .card-front .accent-area {
    position: absolute; right: 20px; top: 90px; width: 330px; height: 250px;
    border-radius: 50%;
    background: radial-gradient(ellipse at 35% 65%, rgba(255,255,255,0.85) 0%, rgba(220,220,220,0.5) 35%, rgba(30,30,30,0.35) 70%, rgba(78,78,80,0) 85%);
  }
  .brand {
    position: absolute; left: 40px; top: 34px; width: 300px;
    display: flex; flex-direction: column; align-items: center;
  }
  .brand .brand-dot {
    width: 26px; height: 26px; border-radius: 50%;
    background: var(--ink-light); margin-bottom: 8px;
  }
  .brand .brand-name {
    font-size: 23px; font-weight: 500; letter-spacing: 1.5px; text-transform: uppercase;
  }
  .brand .brand-rule {
    width: 100%; height: 1px; background: var(--rule-on-dark); margin-top: 4px;
  }
  .brand .brand-sub {
    font-size: 9px; font-weight: 500; letter-spacing: 2px; text-transform: uppercase;
    margin-top: 3px;
  }
  .contact {
    position: absolute; left: 40px; top: 140px;
  }
  .contact .person {
    font-size: 19px; font-weight: 700; letter-spacing: 0.5px; text-transform: uppercase;
  }
  .contact .role {
    font-size: 15px; font-weight: 500; margin-top: 2px; text-transform: uppercase;
  }
  .contact .address {
    font-size: 14px; line-height: 1.35; margin-top: 12px; font-style: normal;
  }
  .contact .links { list-style: none; margin-top: 10px; font-size: 14px; line-height: 1.5; }
  .contact .links li { display: flex; align-items: center; gap: 8px; }
  .contact .links svg { width: 11px; height: 11px; fill: var(--ink-light); flex: none; }
</style>
</head>
<body>
<main class="stage">

  <section class="card card-back" aria-label="Business card, back">
    <div class="watermark-area" role="img" aria-label="Faint clinic emblem decoration"></div>
    <p class="tagline">Personalized Care for Pet's and their People</p>
    <div class="write-lines" aria-hidden="true">
      <span></span><span></span><span></span><span></span><span></span>
    </div>
  </section>

  <section class="card card-front" aria-label="Business card, front">
    <div class="accent-area" role="img" aria-label="Large metallic clinic emblem decoration"></div>

    <div class="brand">
      <span class="brand-dot" aria-hidden="true"></span>
      <span class="brand-name">Kestwick Mews</span>
      <span class="brand-rule" aria-hidden="true"></span>
      <span class="brand-sub">Animal Clinic</span>
    </div>

    <div class="contact">
      <p class="person">Daniel Orrin</p>
      <p class="role">CEO/Founder</p>
      <address class="address">418 Kestwick Lane<br>Toronto Ontario M4T2B8</address>
      <ul class="links">
        <li>
          <svg viewBox="0 0 24 24" aria-hidden="true"><path d="M6.6 10.8a15.1 15.1 0 0 0 6.6 6.6l2.2-2.2a1 1 0 0 1 1-.25 11.4 11.4 0 0 0 3.6.57 1 1 0 0 1 1 1V20a1 1 0 0 1-1 1A17 17 0 0 1 3 4a1 1 0 0 1 1-1h3.5a1 1 0 0 1 1 1c0 1.25.2 2.45.57 3.57a1 1 0 0 1-.25 1z"/></svg>
          416 555 0382
        </li>
        <li>
          <svg viewBox="0 0 24 24" aria-hidden="true"><path d="M2 5h20v14H2z M2 5l10 8 10-8" stroke="#4e4e50" stroke-width="1.5"/></svg>
          kmvc@lorentel.ca
        </li>
        <li>
          <svg viewBox="0 0 24 24" aria-hidden="true"><circle cx="12" cy="12" r="10"/></svg>
          www.kmvc.ca
        </li>
      </ul>
    </div>
  </section>

</main>
</body>
</html>
```